Brovin Terra LLC - Excavation Contractor in Idaho

Wordpress website, visually appealing....Company is Veteran owned business, owner SGT Darrell Oswick NQAF, anything from laser grading to cleaning up your property we do various Skidsteer work and are always buying new attachments to do more jobs. Services include: excavation, grading, snow plowing, demolition and cleanup, fence post hole drilling, trenching.

Target Market(s)

Contractors and Home owners needing projects completed

Industry/Entity Type

Construction

Number of Pages Required

3 page

Font styles to use
Sans Serif

Requirements
Must have
• Site visually appealing and easy to navigate.
Nice to have
• Maybe bold colors?

```html
<!DOCTYPE html>
<html lang="en">
<head>
<meta charset="utf-8">
<title>Brovin Terra LLC – Excavation Contractor in Idaho</title>
<link href="https://fonts.googleapis.com/css2?family=Montserrat:wght@300;400;500;600;700;800&display=swap" rel="stylesheet">
<style>
:root{
  --red:#d7261e;
  --red-dark:#a8161a;
  --ink:#222;
  --text:#777;
  --grey:#e4e4e4;
  --dark:#2b2b2b;
  --white:#fff;
}
*{box-sizing:border-box;margin:0;padding:0}
html,body{width:1200px;height:4721px;overflow:hidden}
body{position:relative;font-family:'Montserrat',sans-serif;color:var(--ink);background:var(--white)}
.abs{position:absolute}
.btn{position:absolute;display:flex;align-items:center;justify-content:center;background:var(--red);color:var(--white);font-size:11px;font-weight:600;border-radius:4px;text-decoration:none}
.btn::before{content:"» ";white-space:pre}
.fill{position:absolute}

/* header */
.topbar{left:300px;top:0;width:900px;height:42px;background:var(--dark);clip-path:polygon(40px 0,100% 0,100% 100%,0 100%)}
.topbar .info{position:absolute;top:12px;color:var(--white);font-size:12px;display:flex;align-items:center;gap:6px}
.dot{width:10px;height:10px;border-radius:50%;background:var(--red);display:inline-block}
.social{position:absolute;top:9px;display:flex;gap:12px;left:1030px}
.social span{width:24px;height:24px;border-radius:50%;background:var(--red);display:block}
.logo{left:70px;top:24px;font-size:30px;font-weight:800;color:var(--dark);letter-spacing:-.5px;display:flex;align-items:center;gap:10px}
.logo i{width:22px;height:22px;background:var(--red);display:block;border-radius:50%}
.nav{left:445px;top:60px;display:flex;gap:18px;font-size:12px}
.nav a{color:#555;text-decoration:none;padding:9px 10px}
.nav a.active{background:var(--red);color:var(--white);border-radius:5px}
.hdr-line{left:0;top:97px;width:1200px;height:1px;background:#ddd}

/* hero */
.hero-photo{left:0;top:98px;width:1200px;height:540px;background:linear-gradient(100deg,#6f6552 0%,#8a7b5e 25%,#c9a340 38%,#7a7a70 55%,#ddd 72%,#f5f5f5 100%)}
.hero-title{right:40px;top:285px;font-size:42px;font-weight:800;color:#1d1d1d}
.hero-sub{right:115px;top:360px;font-size:20px;font-weight:700;color:#1d1d1d}

/* section headings */
.h2{position:absolute;left:0;width:1200px;text-align:center;font-size:34px;font-weight:300;color:#333}
.h2 b{color:var(--red);font-weight:700}
.divider{position:absolute;width:80px;height:14px}
.divider::before{content:"";position:absolute;left:0;right:0;top:6px;height:2px;background:#222}
.divider::after{content:"";position:absolute;left:34px;top:1px;width:10px;height:10px;background:#222;transform:rotate(45deg)}
.lead{position:absolute;left:138px;width:924px;text-align:center;font-size:12.5px;line-height:23px;color:var(--text)}

/* services */
.card{position:absolute;width:279px;text-align:center}
.card .ph{width:279px;height:187px;border-radius:0 0 30px 30px}
.card h3{font-size:17px;font-weight:500;margin-top:10px;color:#222}
.card p{font-size:12px;line-height:23px;color:var(--text);margin-top:8px}
.card a{display:block;margin-top:12px;font-size:11px;color:var(--red);text-decoration:none}

/* about */
.about-bg{left:0;top:1760px;width:1200px;height:520px;background:var(--grey)}
.about-title{left:165px;top:1870px;font-size:34px;font-weight:300;color:#333}
.about-title b{color:var(--red);font-weight:700}
.about-text{left:157px;top:1970px;width:416px;font-size:12.5px;line-height:23.5px;color:var(--text);text-align:justify}

/* gallery */
.gal{position:absolute;top:2442px;width:227px;height:358px}

/* testimonial */
.testi-bg{left:0;top:2930px;width:1200px;height:530px;background:var(--grey)}
.stars{left:537px;top:3194px;display:flex;gap:3px}
.stars svg{width:20px;height:20px}
.quote{left:380px;top:3290px;width:430px;font-size:10.5px;line-height:16px;color:#666}

/* contact */
.contact-title{left:100px;width:280px;text-align:center;font-size:34px;font-weight:300;color:#333}
.c-item{position:absolute;left:138px;display:flex;gap:14px}
.c-icon{width:54px;height:54px;border-radius:50%;background:var(--red);display:flex;align-items:center;justify-content:center}
.c-item h4{font-size:16px;font-weight:700;margin-top:2px}
.c-item p{font-size:12px;line-height:22px;color:#555;margin-top:10px}
.form-box{left:413px;top:3575px;width:554px;height:550px;background:var(--dark)}
.form-title{left:677px;top:3595px;width:296px;text-align:center;font-size:21px;font-weight:700;color:var(--white);line-height:27px}
.form{left:705px;top:3675px;width:237px;height:435px;border:3px solid var(--red);border-radius:6px;padding:16px 18px}
.form label{display:block;font-size:12px;color:var(--white);margin-bottom:3px}
.form .in{background:var(--white);height:32px;font-size:10px;color:#aaa;padding:8px;margin-bottom:15px}
.form .ta{height:74px}
.form .send{position:relative;height:34px;width:100%;font-size:11px}

/* footer */
.foot-bg{left:0;top:4190px;width:1200px;height:531px;background:linear-gradient(180deg,#2d2d2d 0%,#3a2f2e 55%,#b8302a 100%)}
.foot-logo{left:160px;top:4365px;font-size:30px;font-weight:800;color:var(--white);display:flex;align-items:center;gap:10px}
.foot-logo i{width:22px;height:22px;border-radius:50%;background:var(--red);display:block}
.foot-text{left:147px;top:4450px;width:215px;font-size:12px;line-height:23px;color:var(--white);text-align:justify}
.foot-h{font-size:14px;font-weight:700;color:var(--white);text-decoration:underline;position:absolute;top:4330px}
.foot-list{position:absolute;font-size:12px;color:var(--white);line-height:36px}
.foot-list .on{color:var(--red)}
.hours{position:absolute;left:608px;font-size:12px;color:var(--white);line-height:22px;padding-left:24px}
.hours::before{content:"";position:absolute;left:0;top:4px;width:14px;height:14px;border-radius:50%;background:var(--red)}
.fcontact{position:absolute;left:838px;font-size:12px;color:var(--white);display:flex;gap:10px;align-items:center}
.copy{left:0;top:4620px;width:1200px;text-align:center;font-size:12px;color:var(--white)}
</style>
</head>
<body>

<!-- Header -->
<div class="abs topbar">
  <div class="info" style="left:135px"><span class="dot"></span>Cedar Ridge, Idaho 83714</div>
  <div class="info" style="left:355px"><span class="dot"></span>info@brovinterra.com</div>
  <div class="info" style="left:510px"><span class="dot"></span>+1 0208 555 0147</div>
</div>
<div class="social" aria-label="Social links"><span></span><span></span><span></span></div>
<div class="abs logo"><i></i>Brovin Terra LLC</div>
<nav class="abs nav">
  <a class="active">Home</a><a>About Us</a><a>Our Services</a><a>Portfolio</a><a>Contact Us</a>
</nav>
<a class="btn" style="left:1008px;top:60px;width:166px;height:34px">Get Free Quotation</a>
<div class="abs hdr-line"></div>

<!-- Hero -->
<div class="fill hero-photo" role="img" aria-label="Tracked skid steer loader moving soil on a job site"></div>
<svg class="abs" style="left:0;top:540px" width="1200" height="110" viewBox="0 0 1200 110" preserveAspectRatio="none">
  <path d="M0 80 C120 20 230 20 360 50 C500 80 560 10 700 30 C830 45 900 90 1020 40 C1100 10 1160 30 1200 70 L1200 110 L0 110Z" fill="#fff"/>
</svg>
<h1 class="abs hero-title">Welcome To Brovin Terra LLC</h1>
<div class="abs hero-sub">Excavation Contractor In Idaho</div>
<a class="btn" style="left:851px;top:415px;width:122px;height:34px;font-weight:500">Explore More</a>

<!-- Services -->
<h2 class="h2" style="top:705px">How We <b>Serve You</b></h2>
<div class="divider" style="left:560px;top:757px"></div>
<p class="lead" style="top:785px">Lorem ipsum dolor sit amet, consectetur adipiscing elit, sed do eiusmod tempor incididunt ut labore et dolore magna aliqua. Vulputate dignissim suspendisse in est ante. Faucibus turpis in eu mi bibendum neque. Sodales ut etiam sit amet nisl purus. Velit laoreet id donec ultrices tincidunt.</p>

<div class="card" style="left:166px;top:893px"><div class="ph" role="img" aria-label="Excavator bucket digging a lawn" style="background:linear-gradient(160deg,#7b8fa6,#6b7760 55%,#4f6b3a)"></div><h3>Excavation</h3><p>Lorem ipsum dolor sit amet, consectetur adipiscing elit, sed do eiusmod tempor incididunt ut labore et dolore magna aliqua.</p><a>Learn More</a></div>
<div class="card" style="left:460px;top:893px"><div class="ph" role="img" aria-label="Motor grader levelling a gravel road" style="background:linear-gradient(160deg,#d8d6d2,#a59c86 55%,#c8a93c)"></div><h3>Grading</h3><p>Lorem ipsum dolor sit amet, consectetur adipiscing elit, sed do eiusmod tempor incididunt ut labore et dolore magna aliqua.</p><a>Learn More</a></div>
<div class="card" style="left:755px;top:893px"><div class="ph" role="img" aria-label="Loader bucket pushing snow" style="background:linear-gradient(160deg,#e9e9e9,#bdb8b0 50%,#b58a30)"></div><h3>Snow Plowing</h3><p>Lorem ipsum dolor sit amet, consectetur adipiscing elit, sed do eiusmod tempor incididunt ut labore et dolore magna aliqua.</p><a>Learn More</a></div>

<div class="card" style="left:166px;top:1280px"><div class="ph" role="img" aria-label="Excavator demolishing an old building" style="background:linear-gradient(160deg,#a9b3bd,#8c8476 55%,#6e6a60)"></div><h3>Demolition And Cleanup</h3><p>Lorem ipsum dolor sit amet, consectetur adipiscing elit, sed do eiusmod tempor incididunt ut labore et dolore magna aliqua.</p><a>Learn More</a></div>
<div class="card" style="left:460px;top:1280px"><div class="ph" role="img" aria-label="Drill bit boring a fence post hole" style="background:linear-gradient(160deg,#c9ccd0,#7d838a 50%,#3b3f44)"></div><h3>Fence Post Hole Drilling</h3><p>Lorem ipsum dolor sit amet, consectetur adipiscing elit, sed do eiusmod tempor incididunt ut labore et dolore magna aliqua.</p><a>Learn More</a></div>
<div class="card" style="left:755px;top:1280px"><div class="ph" role="img" aria-label="Worker beside a trench with timber and excavator" style="background:linear-gradient(160deg,#b9bcc0,#c79b5a 55%,#8a6a40)"></div><h3>Trenching</h3><p>Lorem ipsum dolor sit amet, consectetur adipiscing elit, sed do eiusmod tempor incididunt ut labore et dolore magna aliqua.</p><a>Learn More</a></div>

<a class="btn" style="left:897px;top:1655px;width:164px;height:35px">Check All Services</a>

<!-- About -->
<div class="fill about-bg"></div>
<svg class="abs" style="left:0;top:1740px" width="1200" height="60" viewBox="0 0 1200 60" preserveAspectRatio="none"><path d="M0 0 L1200 0 L1200 30 C1100 60 1000 10 880 35 C760 60 650 20 520 40 C380 60 280 15 150 35 C80 45 30 30 0 20Z" fill="#fff"/></svg>
<svg class="abs" style="left:0;top:2230px" width="1200" height="60" viewBox="0 0 1200 60" preserveAspectRatio="none"><path d="M0 40 C120 10 240 50 380 25 C520 0 640 45 780 25 C920 5 1060 45 1200 20 L1200 60 L0 60Z" fill="#fff"/></svg>
<h2 class="abs about-title">Welcome To <b>Brovin Terra LLC</b></h2>
<div class="divider" style="left:327px;top:1922px"></div>
<p class="abs about-text">Lorem ipsum dolor sit amet, consectetur adipiscing elit, sed do eiusmod tempor incididunt ut labore et dolore magna aliqua. Vulputate dignissim suspendisse in est ante. Faucibus turpis in eu mi bibendum neque. Sodales ut etiam sit amet nisl purus. Velit laoreet id donec ultrices tincidunt.</p>
<a class="btn" style="left:131px;top:2170px;width:124px;height:35px">Know More</a>
<svg class="abs" style="left:612px;top:1840px" width="360" height="360" viewBox="0 0 360 360">
  <path d="M190 15 A165 165 0 1 0 190 345 A150 165 0 1 1 190 15Z" fill="#d7261e"/>
</svg>
<div class="fill" role="img" aria-label="Yellow excavator working on a sandy site" style="left:635px;top:1845px;width:335px;height:340px;border-radius:50%;background:radial-gradient(circle at 40% 40%,#d6b990,#b9976e 60%,#8f7150)"></div>

<!-- Gallery -->
<h2 class="h2" style="top:2365px">Check Our <b>Gallery</b></h2>
<div class="divider" style="left:560px;top:2416px"></div>
<div class="gal" role="img" aria-label="Excavator arm over dark rocky soil" style="left:139px;background:linear-gradient(170deg,#6d5f4e,#4a3f34 60%,#2e2a26)"></div>
<div class="gal" role="img" aria-label="Grader with yellow blade on dirt" style="left:370px;background:linear-gradient(170deg,#d8dadc,#b3a27a 55%,#8f7a52)"></div>
<div class="gal" role="img" aria-label="Loader bucket in snow" style="left:602px;background:linear-gradient(170deg,#6b5c44,#b18a3a 40%,#dcdcdc 80%)"></div>
<div class="gal" role="img" aria-label="Compact track loader near pine trees" style="left:834px;background:linear-gradient(170deg,#a9b6ab,#3c4a3a 45%,#6a5440)"></div>
<a class="btn" style="left:932px;top:2833px;width:129px;height:35px">Check More</a>

<!-- Testimonial -->
<div class="fill testi-bg"></div>
<svg class="abs" style="left:0;top:2900px" width="1200" height="70" viewBox="0 0 1200 70" preserveAspectRatio="none"><path d="M0 0 L1200 0 L1200 35 C1080 70 960 15 820 40 C680 65 560 20 420 42 C280 64 150 20 0 40Z" fill="#fff"/></svg>
<svg class="abs" style="left:0;top:3420px" width="1200" height="90" viewBox="0 0 1200 90" preserveAspectRatio="none"><path d="M0 50 C150 10 300 60 460 35 C620 10 760 55 920 40 C1050 28 1140 50 1200 40 L1200 90 L0 90Z" fill="#fff"/></svg>
<h2 class="h2" style="top:3040px">Check What Our <b>Client Say</b></h2>
<div class="divider" style="left:560px;top:3090px"></div>
<div class="fill" role="img" aria-label="Client portrait" style="left:380px;top:3150px;width:120px;height:120px;border-radius:50%;background:linear-gradient(160deg,#c9c9c9,#5a5a5a)"></div>
<div class="abs" style="left:537px;top:3175px;font-size:11px;font-weight:600">John Doe</div>
<div class="abs stars">
  <svg viewBox="0 0 20 20"><path d="M10 1l2.6 6 6.4.5-4.9 4.2 1.5 6.3L10 14.6 4.4 18l1.5-6.3L1 7.5 7.4 7z" fill="#f7a600"/></svg>
  <svg viewBox="0 0 20 20"><path d="M10 1l2.6 6 6.4.5-4.9 4.2 1.5 6.3L10 14.6 4.4 18l1.5-6.3L1 7.5 7.4 7z" fill="#f7a600"/></svg>
  <svg viewBox="0 0 20 20"><path d="M10 1l2.6 6 6.4.5-4.9 4.2 1.5 6.3L10 14.6 4.4 18l1.5-6.3L1 7.5 7.4 7z" fill="#f7a600"/></svg>
  <svg viewBox="0 0 20 20"><path d="M10 1l2.6 6 6.4.5-4.9 4.2 1.5 6.3L10 14.6 4.4 18l1.5-6.3L1 7.5 7.4 7z" fill="#f7a600"/></svg>
  <svg viewBox="0 0 20 20"><path d="M10 1l2.6 6 6.4.5-4.9 4.2 1.5 6.3L10 14.6 4.4 18l1.5-6.3L1 7.5 7.4 7z" fill="#f7a600"/></svg>
</div>
<div class="abs" style="left:537px;top:3225px;font-size:9px;color:#999">@username</div>
<div class="abs" style="left:740px;top:3172px;width:76px;height:76px;border-radius:50%;background:var(--red-dark)"></div>
<p class="abs quote">"Lorem ipsum dolor sit amet, consectetur adipiscing elit, sed do eiusmod tempor incididunt ut labore et dolore magna aliqua. Vulputate dignissim suspendisse in est ante. Faucibus turpis in eu mi bibendum neque. Sodales ut etiam sit amet nisl purus. Velit laoreet id donec ultrices tincidunt."</p>
<div class="abs" style="left:568px;top:3357px;display:flex;gap:10px">
  <span style="width:15px;height:15px;border-radius:50%;background:#bbb"></span>
  <span style="width:15px;height:15px;border-radius:50%;background:var(--red-dark)"></span>
  <span style="width:15px;height:15px;border-radius:50%;background:#bbb"></span>
</div>

<!-- Contact -->
<div class="fill" role="img" aria-label="Loader on a snowy construction site" style="left:600px;top:3510px;width:600px;height:675px;background:linear-gradient(150deg,#5b5560,#6e6763 45%,#9a8450 70%,#4a4548)"></div>
<div class="abs contact-title" style="top:3595px">Get In</div>
<div class="abs contact-title" style="top:3636px;color:var(--red);font-weight:700">Touch</div>
<div class="divider" style="left:200px;top:3690px"></div>
<p class="abs" style="left:130px;top:3740px;width:220px;text-align:center;font-size:12.5px;line-height:24px;color:#666">Lorem ipsum dolor sit amet, consectetur adipiscing elit, sed do eiusmod tempor incididunt ut labore et dolore magna aliqua.</p>
<div class="c-item" style="top:3850px"><div class="c-icon"><svg width="22" height="26" viewBox="0 0 22 26"><path d="M11 0C5 0 1 4.5 1 10c0 7 10 16 10 16s10-9 10-16C21 4.5 17 0 11 0z" fill="#fff"/><circle cx="11" cy="10" r="4" fill="#d7261e"/></svg></div><div><h4>Our Address</h4><p>Cedar Ridge,<br>Idaho 83714</p></div></div>
<div class="c-item" style="top:3955px"><div class="c-icon"><svg width="24" height="24" viewBox="0 0 24 24"><path d="M6 2l4 5-2 3c1 3 3 5 6 6l3-2 5 4-3 4C10 22 2 14 2 5z" fill="#fff"/></svg></div><div><h4>Call Us</h4><p>+1 0208 555 0147</p></div></div>
<div class="c-item" style="top:4030px"><div class="c-icon"><svg width="24" height="24" viewBox="0 0 24 24"><path d="M6 2l4 5-2 3c1 3 3 5 6 6l3-2 5 4-3 4C10 22 2 14 2 5z" fill="#fff"/></svg></div><div><h4>Email Us</h4><p>info@brovinterra.com</p></div></div>

<div class="fill form-box"></div>
<div class="fill" role="img" aria-label="Map of the Idaho service area" style="left:420px;top:3583px;width:257px;height:535px;background:linear-gradient(180deg,#d6ecd2,#c3e2c0)"></div>
<div class="abs form-title">Get Free Quotation.<br>Message Us!</div>
<div class="abs form">
  <label>Name</label><div class="in">Name</div>
  <label>Email</label><div class="in">Your Email</div>
  <label>Phone</label><div class="in">Your Phone</div>
  <label>Subject</label><div class="in">Your Subject</div>
  <label>Message</label><div class="in ta">Your Message</div>
  <div class="btn send">Send Your Message</div>
</div>

<!-- Footer -->
<div class="fill foot-bg"></div>
<svg class="abs" style="left:0;top:4170px" width="1200" height="80" viewBox="0 0 1200 80" preserveAspectRatio="none"><path d="M0 0 L1200 0 L1200 40 C1080 75 960 20 820 45 C680 70 540 20 400 45 C260 70 120 25 0 50Z" fill="#fff"/></svg>
<div class="abs foot-logo"><i></i>Brovin Terra LLC</div>
<p class="abs foot-text">Lorem ipsum dolor sit amet, consectetur adipiscing elit, sed do eiusmod tempor incididunt ut labore et dolore magna aliqua. Vulputate dignissim suspendisse in est ante.</p>
<div class="foot-h" style="left:443px">Navigation</div>
<div class="foot-list" style="left:435px;top:4365px"><div class="on">Home</div><div>About Us</div><div>Our Services</div><div>Portfolio</div><div>Contact Us</div></div>
<div class="foot-h" style="left:608px">Working Hour</div>
<div class="hours" style="top:4362px">Monday To Friday<br>7am to 5pm</div>
<div class="hours" style="top:4425px">Saturday<br>Close</div>
<div class="hours" style="top:4487px">Sunday<br>Close</div>
<div class="foot-h" style="left:838px">Contact Us</div>
<div class="fcontact" style="top:4365px"><span class="dot"></span>Cedar Ridge, Idaho 83714</div>
<div class="fcontact" style="top:4403px"><span class="dot"></span>info@brovinterra.com</div>
<div class="fcontact" style="top:4441px"><span class="dot"></span>+1 0208 555 0147</div>
<div class="abs" style="left:840px;top:4478px;display:flex;gap:14px"><span style="width:26px;height:26px;border-radius:50%;background:var(--red)"></span><span style="width:26px;height:26px;border-radius:50%;background:var(--red)"></span><span style="width:26px;height:26px;border-radius:50%;background:var(--red)"></span></div>
<div class="abs copy">Copyright © 2021 Brovin Terra LLC | Powered By Brovin Terra LLC</div>

</body>
</html>
```